Website Design for Bright Hearth e-zine

Website design for e-zine Bright Hearth, providing news and articles for healthy, positive and active family life.

```html
<!DOCTYPE html>
<html lang="en">
<head>
<meta charset="utf-8">
<title>Bright Hearth – family e-zine</title>
<link href="https://fonts.googleapis.com/css2?family=Arimo:wght@400;700&family=Gelasio:wght@400;700&display=swap" rel="stylesheet">
<style>
:root{
  --green:#7ab929;
  --green-dark:#5f9e1c;
  --green-band:#6aaa22;
  --green-text:#5b9a18;
  --orange:#f26a10;
  --orange-ad:#d06000;
  --pale:#f4f8e4;
  --grey-bar:#f2f2f2;
  --ink:#222;
  --muted:#666;
  --footer:#1c2714;
  --fb-blue:#3b5998;
}
*{box-sizing:border-box;margin:0;padding:0}
html,body{width:1200px;height:2649px;overflow:hidden}
body{position:relative;background:var(--green);font-family:Arimo,Arial,sans-serif;color:var(--ink)}
.abs{position:absolute}
.brand{left:0;top:0;width:280px;height:130px;display:flex;align-items:center;padding-left:24px;font-family:Gelasio,serif;font-weight:700;font-size:32px;color:#fff;white-space:nowrap}
.leader-ad{left:281px;top:10px;width:900px;height:110px;background:var(--orange-ad);color:#fff;font-size:13px;font-weight:700;display:flex;align-items:center;justify-content:center}
.main-nav{left:6px;top:137px;width:1188px;height:46px;background:var(--orange);border-top:3px solid #ff8a3a;border-bottom:3px solid #c95206}
.main-nav a{position:absolute;top:8px;font-family:Gelasio,serif;font-size:22px;color:#fff;text-decoration:none;white-space:nowrap}
.page{left:20px;top:183px;width:1160px;height:2167px;background:#fff}
.hero-photo{left:31px;top:205px;width:507px;height:309px;background:linear-gradient(135deg,#c9a64a,#e05a3a 40%,#3a8fc9 70%,#7ab929)}
.hero-list{left:538px;top:205px;width:247px;height:309px;background:#cfe2a6}
.hero-list li{list-style:none;height:61.8px;display:flex;align-items:center;padding-left:16px;font-size:15px;font-weight:700;color:#6a8a2a;border-bottom:1px solid #e4efc8;white-space:nowrap}
.hero-list li.active{background:var(--green-dark);color:#fff;font-weight:400}
.promo{left:798px;top:205px;width:371px;height:309px;background:linear-gradient(160deg,#3f6f72,#2a4f55 60%,#355e5a);border:1px solid #1d3a40}
.today{left:31px;top:536px;font-size:20px}
.cat-band{left:20px;top:573px;width:1160px;height:317px;background:var(--green-band)}
.cat{position:absolute;top:584px;width:180px}
.cat h3{height:24px;font-size:14px;font-weight:400;color:#fff;display:flex;align-items:center;gap:8px;border-bottom:2px solid var(--green-dark);white-space:nowrap}
.cat h3 .arr{width:18px;height:22px;background:var(--green-dark);display:flex;align-items:center;justify-content:center}
.cat .pic{height:224px;border:2px solid #8fc744}
.cat p{margin-top:8px;padding-left:6px;font-size:14px;line-height:25px;color:#eef6df}
.section{position:absolute;left:31px;width:754px;height:459px}
.sec-head{height:35px;background:var(--green);color:#fff;font-size:15px;display:flex;align-items:center;padding-left:16px}
.sec-links{height:35px;background:var(--pale);font-size:12.5px;color:var(--muted);display:flex;align-items:center;padding-left:14px;word-spacing:2px;white-space:nowrap}
.sec-title{position:absolute;left:7px;top:88px;width:300px;font-family:Gelasio,serif;font-weight:700;font-size:19px;line-height:27px;color:var(--green-text)}
.sec-photo{position:absolute;left:13px;top:160px;width:321px;height:240px}
.story{position:absolute;left:359px;width:395px;height:100px}
.story .thumb{position:absolute;left:0;top:0;width:98px;height:98px;background:linear-gradient(135deg,#d8d2c4,#b9c7d8)}
.story p{position:absolute;left:116px;top:14px;width:280px;font-size:14px;line-height:27px;color:var(--green-text)}
.sep{position:absolute;left:356px;width:398px;border-top:1px dashed #999}
.tags{position:absolute;left:0;top:429px;width:754px;height:30px;background:var(--grey-bar);font-size:12.5px;display:flex;align-items:center;padding-left:15px;color:var(--green-text)}
.tags b{color:#555}
.tabs{left:798px;top:907px;width:371px;height:37px;background:var(--green);display:flex}
.tabs span{font-size:17px;font-weight:700;color:#fff;display:flex;align-items:center;padding:0 12px;white-space:nowrap}
.tabs .on{background:var(--orange);width:107px}
.news{left:798px;top:944px;width:371px;height:528px;border:2px solid #a7d06a;border-top:0;padding:5px 12px}
.news li{list-style:none;height:50.7px;border-bottom:2px solid #a7d06a;font-size:14px;font-weight:700;line-height:22px;padding-top:4px;padding-left:5px;color:#2a2a2a}
.fb{left:798px;top:1486px;width:371px;height:503px;border:2px solid var(--fb-blue)}
.fb .av{position:absolute;width:50px;height:48px;background:var(--green);color:#fff;font-family:Gelasio,serif;font-weight:700;font-size:10px;line-height:11px;display:flex;align-items:center;justify-content:center;text-align:center}
.fb .hd{position:absolute;left:74px;top:10px;font-size:13px;color:var(--fb-blue)}
.fb .like{position:absolute;left:76px;top:36px;width:58px;height:22px;border:1px solid #ccd;background:#eef0f6;font-size:12px;color:var(--fb-blue);display:flex;align-items:center;justify-content:center}
.fb .post{position:absolute;left:74px;top:80px;width:285px;font-size:12px;line-height:20px;color:#222}
.fb .post h4{font-size:13px;color:var(--fb-blue);line-height:19px;margin-bottom:4px}
.fb .count{position:absolute;left:13px;top:292px;font-size:13px;width:345px;border-top:1px solid #e5e5e5;padding-top:8px}
.fans{position:absolute;left:13px;top:318px;display:grid;grid-template-columns:repeat(5,64px);column-gap:4px;row-gap:6px}
.fans div{width:64px;text-align:center;font-size:11px;color:#777;white-space:nowrap}
.fans i{display:block;height:62px;margin-bottom:4px}
.follow{left:905px;top:2010px;width:170px;height:120px;background:radial-gradient(ellipse at 50% 45%,#e8b060 0,#9ccbe8 45%,#fff 72%)}
.footer{left:20px;top:2350px;width:1160px;height:223px;background:var(--footer)}
.footer ul{position:absolute;top:26px;list-style:none}
.footer li{font-size:14.5px;color:#fff;line-height:31px}
.legal{left:43px;top:2582px;color:#fff;font-size:14px;font-weight:700}
.legal-links{left:43px;top:2611px;color:#f4f8e4;font-size:14px}
</style>
</head>
<body>
<header>
  <div class="abs brand">Bright Hearth</div>
  <div class="abs leader-ad">728x90</div>
  <nav class="abs main-nav">
    <a style="left:56px">Home</a><a style="left:149px">Children</a><a style="left:267px">Healthy life</a><a style="left:414px">Family travels</a><a style="left:585px">Marriage advices</a><a style="left:784px">Housekeeping</a><a style="left:958px">Food &amp; drinks</a>
  </nav>
</header>

<div class="abs page"></div>

<div class="abs hero-photo" role="img" aria-label="Family playing together in a colourful ball pit"></div>
<ul class="abs hero-list">
  <li>Lorem ipsum dolor sit amet</li>
  <li class="active">Lorem ipsum dolor sit amet</li>
  <li>Lorem ipsum dolor sit amet</li>
  <li>Lorem ipsum dolor sit amet</li>
  <li>Lorem ipsum dolor sit amet</li>
</ul>
<aside class="abs promo" role="img" aria-label="Advertisement for a children's health product with hand-lettered slogan and product packs"></aside>

<div class="abs today">Today: November 11, 2011</div>

<div class="abs cat-band"></div>
<div class="cat" style="left:33px"><h3><span class="arr"><svg width="8" height="12"><path d="M1 1l5 5-5 5" stroke="#fff" fill="none" stroke-width="1.5"/></svg></span>CHILDREN</h3><div class="pic" role="img" aria-label="Smiling children sitting together" style="background:linear-gradient(90deg,#3aa54a,#f08c2a,#e04a8a,#7a5ad0)"></div><p>Duis aute irure dolor in reprehenderit</p></div>
<div class="cat" style="left:225px"><h3><span class="arr"><svg width="8" height="12"><path d="M1 1l5 5-5 5" stroke="#fff" fill="none" stroke-width="1.5"/></svg></span>HEALTHY LIFE</h3><div class="pic" role="img" aria-label="Fresh vegetables" style="background:linear-gradient(135deg,#d83a2a,#4a9a2a,#f0c030)"></div><p>Duis aute irure dolor in reprehenderit</p></div>
<div class="cat" style="left:417px"><h3><span class="arr"><svg width="8" height="12"><path d="M1 1l5 5-5 5" stroke="#fff" fill="none" stroke-width="1.5"/></svg></span>FAMILY TRAVELS</h3><div class="pic" role="img" aria-label="Suitcases and a straw hat" style="background:linear-gradient(180deg,#fff 40%,#8a5a2a)"></div><p>Duis aute irure dolor in reprehenderit</p></div>
<div class="cat" style="left:608px"><h3><span class="arr"><svg width="8" height="12"><path d="M1 1l5 5-5 5" stroke="#fff" fill="none" stroke-width="1.5"/></svg></span>MARRIAGE ADVIDES</h3><div class="pic" role="img" aria-label="Wedding couple with family" style="background:linear-gradient(90deg,#2a2a2a,#e8e4dc,#3a3a3a)"></div><p>Duis aute irure dolor in reprehenderit</p></div>
<div class="cat" style="left:800px"><h3><span class="arr"><svg width="8" height="12"><path d="M1 1l5 5-5 5" stroke="#fff" fill="none" stroke-width="1.5"/></svg></span>HOUSE KEEPING</h3><div class="pic" role="img" aria-label="Cleaning with yellow gloves" style="background:linear-gradient(180deg,#4a4a4a,#e8d020 60%,#7a7aa0)"></div><p>Duis aute irure dolor in reprehenderit</p></div>
<div class="cat" style="left:992px"><h3><span class="arr"><svg width="8" height="12"><path d="M1 1l5 5-5 5" stroke="#fff" fill="none" stroke-width="1.5"/></svg></span>FOOD &amp; DRINKS</h3><div class="pic" role="img" aria-label="Plate of fried food with a drink" style="background:linear-gradient(180deg,#dfe6ea,#d8a050 55%,#c83a2a)"></div><p>Duis aute irure dolor in reprehenderit</p></div>

<section class="section" style="top:907px">
  <div class="sec-head">CHILDREN</div>
  <div class="sec-links">Children Health &nbsp;|&nbsp; Children Life &nbsp;|&nbsp; Children GrowUp &nbsp;|&nbsp; Baby Care &nbsp;|&nbsp; Children Toys &nbsp;|&nbsp; Food for Baby</div>
  <h2 class="sec-title">Lorem ipsum dolor sit amet, consectetur adipisicing elit</h2>
  <div class="sec-photo" role="img" aria-label="Group of children posing outdoors" style="background:linear-gradient(135deg,#6a7a8a,#c84a3a,#3a6ab0)"></div>
  <div class="story" style="top:99px"><div class="thumb" role="img" aria-label="Globe surrounded by children"></div><p>Lorem ipsum dolor sit amet, consectetur adipisicing elit</p></div>
  <div class="sep" style="top:201px"></div>
  <div class="story" style="top:211px"><div class="thumb" role="img" aria-label="Two toddlers in green and orange"></div><p>Lorem ipsum dolor sit amet, consectetur adipisicing elit</p></div>
  <div class="sep" style="top:313px"></div>
  <div class="story" style="top:320px"><div class="thumb" role="img" aria-label="Child standing with a hoop"></div><p>Lorem ipsum dolor sit amet, consectetur adipisicing elit</p></div>
  <div class="tags"><b>Tag clouds</b>: feeding, nutrition for children, colostrum</div>
</section>

<section class="section" style="top:1380px">
  <div class="sec-head">HEALTHY LIFE</div>
  <div class="sec-links">Children Health &nbsp;|&nbsp; Children Life &nbsp;|&nbsp; Children GrowUp &nbsp;|&nbsp; Baby Care &nbsp;|&nbsp; Children Toys &nbsp;|&nbsp; Food for Baby</div>
  <h2 class="sec-title">Lorem ipsum dolor sit amet, consectetur adipisicing elit</h2>
  <div class="sec-photo" role="img" aria-label="Woman stretching on grass under a blue sky" style="background:linear-gradient(180deg,#2a6ad8,#8ab8f0 65%,#5a9a2a)"></div>
  <div class="story" style="top:99px"><div class="thumb" role="img" aria-label="Globe surrounded by children"></div><p>Lorem ipsum dolor sit amet, consectetur adipisicing elit</p></div>
  <div class="sep" style="top:201px"></div>
  <div class="story" style="top:211px"><div class="thumb" role="img" aria-label="Two toddlers in green and orange"></div><p>Lorem ipsum dolor sit amet, consectetur adipisicing elit</p></div>
  <div class="sep" style="top:313px"></div>
  <div class="story" style="top:320px"><div class="thumb" role="img" aria-label="Child standing with a hoop"></div><p>Lorem ipsum dolor sit amet, consectetur adipisicing elit</p></div>
  <div class="tags"><b>Tag clouds</b>: feeding, nutrition for children, colostrum</div>
</section>

<section class="section" style="top:1852px">
  <div class="sec-head">HEALTHY LIFE</div>
  <div class="sec-links">Children Health &nbsp;|&nbsp; Children Life &nbsp;|&nbsp; Children GrowUp &nbsp;|&nbsp; Baby Care &nbsp;|&nbsp; Children Toys &nbsp;|&nbsp; Food for Baby</div>
  <h2 class="sec-title">Lorem ipsum dolor sit amet, consectetur adipisicing elit</h2>
  <div class="sec-photo" role="img" aria-label="Woman stretching on grass under a blue sky" style="background:linear-gradient(180deg,#2a6ad8,#8ab8f0 65%,#5a9a2a)"></div>
  <div class="story" style="top:99px"><div class="thumb" role="img" aria-label="Globe surrounded by children"></div><p>Lorem ipsum dolor sit amet, consectetur adipisicing elit</p></div>
  <div class="sep" style="top:201px"></div>
  <div class="story" style="top:211px"><div class="thumb" role="img" aria-label="Two toddlers in green and orange"></div><p>Lorem ipsum dolor sit amet, consectetur adipisicing elit</p></div>
  <div class="sep" style="top:313px"></div>
  <div class="story" style="top:320px"><div class="thumb" role="img" aria-label="Child standing with a hoop"></div><p>Lorem ipsum dolor sit amet, consectetur adipisicing elit</p></div>
  <div class="tags"><b>Tag clouds</b>: feeding, nutrition for children, colostrum</div>
</section>

<div class="abs tabs"><span class="on">Hot news</span><span>Top Weeks</span><span>Top Month</span></div>
<ul class="abs news">
  <li>Lorem ipsum dolor sit amet, consectetur adipisicing elit, sed do.</li>
  <li>Lorem ipsum dolor sit amet, consectetur adipisicing elit, sed do.</li>
  <li>Lorem ipsum dolor sit amet, consectetur adipisicing elit, sed do.</li>
  <li>Lorem ipsum dolor sit amet, consectetur adipisicing elit, sed do.</li>
  <li>Lorem ipsum dolor sit amet, consectetur adipisicing elit, sed do.</li>
  <li>Lorem ipsum dolor sit amet, consectetur adipisicing elit, sed do.</li>
  <li>Lorem ipsum dolor sit amet, consectetur adipisicing elit, sed do.</li>
  <li>Lorem ipsum dolor sit amet, consectetur adipisicing elit, sed do.</li>
  <li>Lorem ipsum dolor sit amet, consectetur adipisicing elit, sed do.</li>
  <li style="border-bottom:0">Lorem ipsum dolor sit amet, consectetur adipisicing elit, sed do.</li>
</ul>

<aside class="abs fb">
  <div class="av" style="left:10px;top:12px">Bright Hearth</div>
  <div class="hd"><b>Bright Hearth</b> on Friendbook</div>
  <div class="like">Like</div>
  <div class="av" style="left:10px;top:80px">Bright Hearth</div>
  <div class="post"><h4>Lorem ipsum dolor sit amet, consectetur adipisicing elit</h4>Sed do eiusmod tempor incididunt ut labore et dolore magna aliqua. Ut enim ad minim veniam, quis nostrud exercitation ullamco laboris nisi ut aliquip ex ea commodo consequat. Duis aute irure dolor in reprehenderit in voluptate velit esse cillum dolore eu fugiat nulla pariatur. Excepteur sint occaecat cupidatat non</div>
  <div class="count">3,518 people like <b>Bright Hearth</b></div>
  <div class="fans">
    <div><i role="img" aria-label="Fan photo" style="background:#d89a8a"></i>Taren</div>
    <div><i role="img" aria-label="Fan photo" style="background:#c8b8a8"></i>Pholan</div>
    <div><i role="img" aria-label="Fan photo" style="background:#4a6aa0"></i>Ngal</div>
    <div><i role="img" aria-label="Fan photo" style="background:#3a3a3a"></i>Kiro</div>
    <div><i role="img" aria-label="Fan photo" style="background:#c85a4a"></i>Thanh Vy</div>
    <div><i role="img" aria-label="Fan photo" style="background:#e8e4e0"></i>Nhan</div>
    <div><i role="img" aria-label="Fan photo" style="background:#d8a878"></i>Hoa</div>
    <div><i role="img" aria-label="Fan photo" style="background:#a04a1a"></i>Mira</div>
    <div><i role="img" aria-label="Fan photo" style="background:#4aa03a"></i>Xenia</div>
    <div><i role="img" aria-label="Fan photo" style="background:#b8d0a0"></i>Khanh</div>
  </div>
</aside>

<div class="abs follow" role="img" aria-label="Illustration of two birds on a wooden follow sign"></div>

<footer class="abs footer">
  <ul style="left:58px"><li>Children</li><li>Healthy life</li><li>Family travels</li><li>Marriage advices</li><li>Housekeeping</li><li>Food &amp; drinks</li></ul>
  <ul style="left:264px"><li>About Us</li><li>Contact Us</li><li>Advertise</li><li>SiteMap</li></ul>
  <ul style="left:456px"><li>Friendbook</li><li>Chirper</li></ul>
</footer>
<div class="abs legal">© 2011 Bright Hearth. All Rights Reserved</div>
<div class="abs legal-links">Privacy - Terms of Use</div>
</body>
</html>
```